Professional and creative business card design for recruiting service providers

Our company supports German medium-sized companies in filling vacancies promptly. For this we use social media marketing and bring our customers into the visibility.

We want a professional but also creative design for our business cards.

Please look at valdringer-kollegen.de to get an impression of our CI.

Target Market(s)

Small and medium-sized companies in Germany from the industry

Industry/Entity Type

Industrie, Handwerk

Contact Information for Business Card

Name, Position, Telefonnummer, Email, Website

Colors
EE7325
F08F49
F5BC92
FAE3D3
FDF4ED

Requirements
Must have
• A picture of the employee and in the style of www.valdringer-kollegen.de

```html
<!DOCTYPE html>
<html lang="de">
<head>
<meta charset="utf-8">
<title>Valdringer &amp; Kollegen – Visitenkarte</title>
<link rel="stylesheet" href="https://fonts.googleapis.com/css2?family=Montserrat:wght@400;500;700;800&display=swap">
<style>
  :root {
    --bg: #d6d6d6;
    --card-white: #ffffff;
    --card-black: #262626;
    --ink: #262626;
    --emboss: #1c1c1c;
    --emboss-hi: #343434;
    --orange: #f06030;
    --orange-soft: #f5bc92;
    --grey-text: #3a3a3a;
  }
  * { margin: 0; padding: 0; box-sizing: border-box; }
  html, body { width: 1200px; height: 788px; overflow: hidden; }
  body {
    background: var(--bg);
    font-family: "Montserrat", sans-serif;
    position: relative;
  }
  .card {
    position: absolute;
    top: 239px;
    width: 540px;
    height: 310px;
    border-radius: 22px;
    box-shadow: 0 14px 34px rgba(0,0,0,0.22);
    overflow: hidden;
  }
  .card-front { left: 40px; background: var(--card-white); }
  .card-back { left: 620px; background: var(--card-black); }

  .brand {
    position: absolute;
    left: 40px;
    top: 44px;
    display: flex;
    align-items: center;
    gap: 14px;
  }
  .brand-square {
    width: 44px; height: 44px;
    background: var(--orange);
  }
  .brand-name {
    font-weight: 700;
    font-size: 19px;
    line-height: 1.08;
    letter-spacing: 1.5px;
    color: var(--ink);
    text-transform: uppercase;
  }
  .person { position: absolute; left: 40px; top: 138px; }
  .person-name {
    font-weight: 700;
    font-size: 19px;
    letter-spacing: 1px;
    color: var(--orange);
    text-transform: uppercase;
  }
  .person-role {
    font-weight: 500;
    font-size: 14px;
    color: var(--grey-text);
    margin-top: 2px;
  }
  .contact {
    position: absolute;
    left: 40px;
    top: 202px;
    list-style: none;
  }
  .contact li {
    display: flex;
    align-items: center;
    gap: 9px;
    font-size: 14px;
    color: var(--grey-text);
    line-height: 24px;
  }
  .contact svg { width: 12px; height: 12px; fill: var(--orange); flex: none; }
  .employee-photo {
    position: absolute;
    right: 48px;
    top: 56px;
    width: 180px;
    height: 198px;
    border-radius: 10px;
    background: linear-gradient(160deg, var(--orange-soft) 0%, var(--orange) 55%, var(--ink) 100%);
  }

  .back-brand {
    position: absolute;
    inset: 0;
    display: flex;
    align-items: center;
    justify-content: center;
    gap: 22px;
  }
  .back-square {
    width: 84px; height: 84px;
    background: var(--emboss);
    box-shadow: 1px 1px 0 var(--emboss-hi);
  }
  .back-name {
    font-weight: 800;
    font-size: 34px;
    line-height: 1.05;
    letter-spacing: 2px;
    color: var(--emboss);
    text-shadow: 1px 1px 0 var(--emboss-hi);
    text-transform: uppercase;
  }
</style>
</head>
<body>
  <section class="card card-front">
    <div class="brand">
      <div class="brand-square"></div>
      <div class="brand-name">Valdringer<br>&amp; Kollegen</div>
    </div>
    <div class="person">
      <div class="person-name">Jonas Valdringer</div>
      <div class="person-role">Gründer</div>
    </div>
    <ul class="contact">
      <li><svg viewBox="0 0 12 12"><path d="M2.5 0.5 4.5 3 3.3 4.4c.7 1.7 2.3 3.3 4.3 4.3L9 7.5l2.5 2-1.3 2C5.5 11.3.7 6.5.5 1.8z"/></svg>(123) 456 7890</li>
      <li><svg viewBox="0 0 12 12"><path d="M0 2h12v1.2L6 7 0 3.2zM0 4.6l6 3.8 6-3.8V10H0z"/></svg>info@valdringer-kollegen.de</li>
      <li><svg viewBox="0 0 12 12"><circle cx="6" cy="6" r="6"/></svg>www.valdringer-kollegen.de</li>
    </ul>
    <div class="employee-photo" role="img" aria-label="Porträtfoto des Mitarbeiters Jonas Valdringer"></div>
  </section>

  <section class="card card-back">
    <div class="back-brand">
      <div class="back-square"></div>
      <div class="back-name">Valdringer<br>&amp; Kollegen</div>
    </div>
  </section>
</body>
</html>
```